Nanotechnology meets nature cosmetic company needs label design. Name of the company is QuillaBloom

We are a cosmetic brand that combines nanotechnology with nature in the form of hemp extracts and essential oils, creating products that provide pain relief as well as stress reduction and relaxation. We have three different products and need three separate labels. We have a logo and would like to incorporate that into the label design. The colors are teal, black and gray. We would like to convey a message of combining nature with cutting edge cosmetic technology.
1. Topical pain lotion
2. Bath soak
3. Massage lotion
The logo is attached and I would just like the logo used and not the text below. The colors of the logo should be teal cross and "V" inside the gray lines that make up the circle with black color inside the circle. If this can't be done, I can send another logo.

```html
<!DOCTYPE html>
<html lang="en">
<head>
<meta charset="UTF-8">
<title>QuillaBloom Topical Pain Lotion Label</title>
<link rel="stylesheet" href="https://fonts.googleapis.com/css2?family=Poppins:wght@400;500;600;700&family=Allura&display=swap">
<style>
  :root {
    --page: #ffffff;
    --band-black: #2a2b2d;
    --teal-light: #6fd3c6;
    --teal: #17ab9a;
    --teal-deep: #139a8a;
    --text-light: #f1f3f3;
    --ink: #1f2324;
    --ring-gray: #8e9092;
    --mark-fill: #1c1d1f;
  }
  html, body {
    margin: 0;
    padding: 0;
    width: 1200px;
    height: 1200px;
    overflow: hidden;
    background: var(--page);
  }
  .canvas {
    position: relative;
    width: 1200px;
    height: 1200px;
  }
  .label {
    position: absolute;
    left: 280px;
    top: 30px;
    width: 640px;
    height: 1140px;
    background: linear-gradient(90deg, var(--teal) 0%, var(--teal-light) 22%, var(--teal) 55%, var(--teal-deep) 100%);
    overflow: hidden;
    font-family: "Poppins", sans-serif;
    color: var(--text-light);
    text-align: center;
  }
  .label__band {
    position: absolute;
    left: 0;
    top: 0;
    width: 100%;
    height: 228px;
    background: var(--band-black);
  }
  .label__mark {
    position: absolute;
    left: 170px;
    top: 78px;
    width: 300px;
    height: 300px;
  }
  .label__brand {
    position: absolute;
    left: 0;
    width: 100%;
    top: 412px;
    margin: 0;
    font-size: 44px;
    font-weight: 600;
    letter-spacing: -0.5px;
  }
  .label__title {
    position: absolute;
    left: 0;
    width: 100%;
    top: 520px;
    margin: 0;
    font-size: 112px;
    font-weight: 700;
    line-height: 116px;
    letter-spacing: 1px;
  }
  .label__type {
    position: absolute;
    left: 0;
    width: 100%;
    top: 780px;
    margin: 0;
    font-family: "Allura", cursive;
    font-size: 120px;
    line-height: 120px;
    color: var(--ink);
  }
  .label__desc {
    position: absolute;
    left: 0;
    width: 100%;
    top: 936px;
    margin: 0;
    font-size: 28px;
    font-weight: 400;
    line-height: 37px;
  }
  .label__volume {
    position: absolute;
    left: 0;
    width: 100%;
    top: 1056px;
    margin: 0;
    font-size: 27px;
    font-weight: 400;
  }
</style>
</head>
<body>
<div class="canvas">
  <section class="label">
    <div class="label__band"></div>
    <svg class="label__mark" viewBox="0 0 300 300" aria-hidden="true">
      <circle cx="150" cy="150" r="140" fill="var(--mark-fill)" stroke="var(--ring-gray)" stroke-width="10"/>
    </svg>
    <p class="label__brand">QuillaBloom</p>
    <h1 class="label__title">TOPICAL<br>PAIN</h1>
    <p class="label__type">lotion</p>
    <p class="label__desc">PAIN RELIEF FORMULA WITH<br>HEMP EXTRACTS AND ESSENTIAL OILS</p>
    <p class="label__volume">NET.WT.100ML</p>
  </section>
</div>
</body>
</html>
```